Layout of a 14-page report

I need a professional, well-designed, layout for a 14-page free report I'm offering.
My colors are red/black/white and have a chalkboard theme in my header graphic which you can incorporate if you want: see my website here - http://larkavell.example/. I am an SEO strategy consultant and this report is about "Ranking Basics."
The attachment contains a few images/designs and graphics I like that may help guide your creative process.
I would like to see the:
1. Cover page
2. inside spread layout of a standard page
3. inside spread layout of a "page with sidebar content" (indicated in the attachment)
The selected winner will complete all pages. Thank you!

```html
<!DOCTYPE html>
<html lang="en">
<head>
<meta charset="utf-8">
<title>Lark Avell – Getting Serious about SEO</title>
<link rel="stylesheet" href="https://fonts.googleapis.com/css2?family=Questrial&family=Open+Sans:wght@400;700&display=swap">
<style>
  :root {
    --backdrop: #dcdee2;
    --board-dark: #2a2a2a;
    --board-mid: #3d3d3d;
    --chalk: #f2f2f2;
    --chalk-soft: #cfcfcf;
    --brand-red: #e3252b;
    --brand-red-deep: #9b1a20;
    --bubble-grey: rgba(200, 200, 200, 0.5);
    --bubble-light: rgba(225, 225, 225, 0.68);
    --bubble-blue: #2a5c8c;
    --photo-warm: #b88c74;
    --photo-blush: #e2b4ab;
  }
  html, body {
    margin: 0;
    width: 1200px;
    height: 817px;
    overflow: hidden;
    background: var(--backdrop);
  }
  .cover {
    position: absolute;
    left: 320px;
    top: 18px;
    width: 560px;
    height: 780px;
    overflow: hidden;
    background: radial-gradient(ellipse at 30% 25%, var(--board-mid), var(--board-dark) 75%);
    box-shadow: 0 6px 24px rgba(0,0,0,0.25);
  }
  .cover-art {
    position: absolute;
    inset: 0;
  }
  .author-photo {
    position: absolute;
    left: 300px;
    top: 20px;
    width: 220px;
    height: 260px;
    background: linear-gradient(180deg, var(--photo-warm) 0%, var(--photo-blush) 65%, #d98f92 100%);
  }
  .cover-text {
    position: absolute;
    left: 40px;
    top: 150px;
    width: 250px;
    color: var(--chalk);
  }
  .author-name {
    margin: 0 0 28px;
    font-family: "Questrial", sans-serif;
    font-weight: 400;
    font-size: 50px;
    letter-spacing: 0.5px;
    line-height: 1;
    white-space: nowrap;
  }
  .report-title {
    margin: 0 0 8px;
    font-family: "Open Sans", sans-serif;
    font-weight: 700;
    font-size: 17px;
  }
  .report-sub {
    margin: 0 0 12px;
    font-family: "Questrial", sans-serif;
    font-size: 16px;
    line-height: 1.25;
    color: var(--chalk-soft);
  }
  .bubble-label {
    font-family: "Questrial", sans-serif;
    fill: var(--chalk);
    text-anchor: middle;
    dominant-baseline: middle;
  }
  .bubble-label.dark { fill: var(--board-dark); }
  .year-label {
    font-family: "Questrial", sans-serif;
    font-size: 40px;
    fill: #555;
    text-anchor: middle;
    dominant-baseline: middle;
  }
  .studio-mark {
    position: absolute;
    left: 450px;
    top: 690px;
    width: 86px;
    height: 54px;
    background: var(--chalk);
    display: flex;
    align-items: center;
    justify-content: center;
    font-family: "Questrial", sans-serif;
    font-size: 17px;
    color: var(--board-dark);
  }
</style>
</head>
<body>
  <main class="cover">
    <div class="author-photo" role="img" aria-label="Portrait photograph of the author, smiling, shoulders up"></div>

    <svg class="cover-art" viewBox="0 0 560 780" aria-hidden="true">
      <path d="M0 720 C 110 520, 290 350, 560 250 L 560 282 C 310 380, 140 540, 45 780 L 0 780 Z" fill="var(--brand-red)" opacity="0.92"/>
      <path d="M300 280 C 390 230, 470 205, 560 185 L 560 250 C 470 270, 390 300, 330 335 Z" fill="var(--brand-red-deep)" opacity="0.45"/>
      <ellipse cx="330" cy="860" rx="420" ry="200" fill="#333" opacity="0.6"/>
    </svg>

    <svg class="cover-art" viewBox="0 0 560 780" aria-hidden="true">
      <g class="bubbles">
        <circle cx="488" cy="318" r="22" fill="var(--bubble-grey)"/>
        <circle cx="250" cy="430" r="55" fill="var(--bubble-grey)"/>
        <circle cx="385" cy="365" r="62" fill="var(--bubble-grey)"/>
        <circle cx="462" cy="440" r="95" fill="var(--bubble-light)"/>
        <circle cx="305" cy="470" r="45" fill="var(--bubble-blue)"/>
        <circle cx="392" cy="490" r="55" fill="var(--brand-red-deep)" opacity="0.85"/>
        <circle cx="480" cy="535" r="50" fill="var(--bubble-blue)"/>
        <circle cx="280" cy="560" r="65" fill="var(--bubble-grey)"/>
        <circle cx="368" cy="560" r="35" fill="var(--brand-red-deep)" opacity="0.55"/>
        <circle cx="410" cy="595" r="35" fill="var(--bubble-grey)"/>
        <circle cx="350" cy="672" r="70" fill="var(--bubble-grey)" opacity="0.7"/>
      </g>
      <g class="bubble-labels">
        <text class="bubble-label dark" x="488" y="319" font-size="20">@</text>
        <text class="bubble-label" x="232" y="418" font-size="14">Wrenly</text>
        <text class="bubble-label" x="372" y="340" font-size="15">Wrenly</text>
        <text class="bubble-label dark" x="500" y="420" font-size="22">Gatherly</text>
        <text class="bubble-label" x="300" y="470" font-size="11">Gatherly</text>
        <text class="bubble-label" x="392" y="492" font-size="14">Orbitly</text>
        <text class="bubble-label" x="484" y="540" font-size="12">Guildway</text>
        <g fill="none" stroke="#333" stroke-width="2">
          <rect x="244" y="540" width="62" height="40"/>
          <path d="M244 540 L275 565 L306 540"/>
        </g>
        <text class="bubble-label dark" x="410" y="596" font-size="28">@</text>
        <text class="year-label" x="350" y="676">2015</text>
      </g>
    </svg>

    <div class="cover-text">
      <h1 class="author-name">Lark Avell</h1>
      <p class="report-title">Getting Serious about SEO:</p>
      <p class="report-sub">How to Get More Leads<br>A Checklist of 8 Essentials</p>
      <p class="report-sub">for Busy Marketers in<br>Growing Businesses</p>
    </div>

    <div class="studio-mark">Halden</div>
  </main>
</body>
</html>
```